Lumaform website scandinavian interior design

Existing website: http://lumaform-example.no/

Webdesign for interior designer Ragna Tvedtholm. The company name is Lumaform. Scandinavian interiør is known to be simple and elegant. The website will be in Norwegian, we are working on the text. The website needs to have a few more pages than just the front page. Here are the different titles of the pages:

1. Hjem
2. Om Lumaform
3. Tjenester og priser
4.. Kontakt oss

There should be Facebook and Instagram icons somewhere at the bottom of the website.

The logo we want to use is attached (pink with black print, see attachment )

We have attached images for inspiration. We want to use some of these colors. The color in the logo, The style should be elegant, modern and delicate.

It is imprtant that the website is user friendly.

Target Market(s)

People who want to decorate their home
Companies and public sector who need to redecorate

Industry/Entity Type

Interior Designer

Coding

Coded - Design and coding required

Number of Pages Required

5+ page

Font styles to use
Other font styles liked:
• see example in the logo breakdown

Requirements
Must have
• Elegant, modern and delicate design
Images of design, see examples attached
Colors similar to the pictures
Should not have
• Too bright colors
Pictures of people

```html
<!DOCTYPE html>
<html lang="no">
<head>
<meta charset="utf-8">
<title>Lumaform – Farge &amp; Interiørdesign</title>
<link href="https://fonts.googleapis.com/css2?family=Parisienne&family=Poppins:wght@300;400;500;600&display=swap" rel="stylesheet">
<style>
:root{
  --maroon:#6b1f17;
  --maroon-soft:rgba(107,31,23,.86);
  --ink:#1d2b2f;
  --night:#13242b;
  --blush:#f4dede;
  --blush-line:#f0d6d2;
  --grey-line:#c9c9c9;
  --white:#ffffff;
  --text:#2b2b2b;
}
*{margin:0;padding:0;box-sizing:border-box}
html,body{width:1200px;height:2722px;overflow:hidden;background:var(--white)}
body{position:relative;font-family:'Poppins',sans-serif;color:var(--text);font-weight:300}
.abs{position:absolute}
.script{font-family:'Parisienne',cursive;font-weight:400;color:var(--ink)}
.btn{position:absolute;background:var(--maroon);color:var(--white);font-size:11.5px;font-weight:400;display:flex;align-items:center;justify-content:center;letter-spacing:.2px}
.placeholder{position:absolute}

/* hero */
.hero{left:0;top:0;width:1200px;height:613px;background:linear-gradient(115deg,#d9d9d7 0%,#eeeeec 35%,#f5f4f1 55%,#dcdad4 80%,#c9c7c1 100%)}
.logo-box{left:118px;top:0;width:174px;height:156px;background:var(--blush);display:flex;flex-direction:column;align-items:center;justify-content:center;gap:6px}
.logo-name{font-family:'Poppins',sans-serif;font-size:24px;font-weight:500;color:var(--ink);letter-spacing:.5px}
.logo-tag{font-size:7px;letter-spacing:1.6px;color:var(--maroon);font-weight:400}
.nav{left:614px;top:70px;display:flex;gap:32px;font-size:11.5px;color:var(--ink)}
.nav a{color:inherit;text-decoration:none}
.nav .active{font-weight:600}
.flag{left:1059px;top:70px}
.hero-title{left:0;width:1200px;top:190px;text-align:center;font-size:52px;line-height:62px}
.hero-text{left:0;width:1200px;top:334px;text-align:center;font-size:12px;line-height:27px;color:var(--ink)}
.arrow{top:308px}

/* welcome */
.welcome-title{left:148px;top:640px;font-size:56px}
.welcome-text{left:149px;top:726px;width:490px;font-size:12px;line-height:25.6px;color:var(--ink)}

/* business */
.biz-title{left:0;width:1200px;top:1030px;text-align:center;font-size:58px;color:var(--white)}
.biz-text{left:0;width:1200px;top:1115px;text-align:center;font-size:12px;line-height:26px;color:var(--white)}
.service{top:1202px;height:139px;border:2px solid var(--white);display:flex;flex-direction:column;align-items:center;justify-content:flex-end;padding-bottom:30px;gap:14px;color:var(--white);font-size:11px;font-weight:400}
.service .icon{width:62px;height:62px;border:1px solid rgba(255,255,255,.55);border-radius:4px;background:rgba(255,255,255,.08)}

/* private */
.priv-title{left:583px;top:1500px;font-size:54px}
.priv-text{left:584px;top:1583px;width:460px;font-size:12px;line-height:25.6px;color:var(--ink)}

/* feature cards */
.feat-title{left:168px;top:1945px;font-size:60px;color:var(--white)}
.card{padding:28px 44px 0 41px}
.card h3{font-size:14px;font-weight:500;letter-spacing:.3px;margin-bottom:14px}
.card p{font-size:12px;line-height:25.6px}
.card-light{background:var(--white);color:var(--ink)}
.card-dark{background:var(--maroon);color:var(--white)}

/* footer */
.foot-head{left:166px;top:2453px;font-size:14px;font-weight:600;color:var(--white);letter-spacing:.5px}
.foot-addr{left:167px;top:2500px;font-size:12.5px;line-height:26.5px;color:var(--white);font-weight:400}
.foot-logo{left:483px;top:2400px;width:200px;text-align:center;color:var(--white)}
.foot-logo .logo-name{color:var(--white);font-size:30px}
.foot-logo .logo-tag{color:#cfd6d8;display:block;margin-top:6px}
.foot-copy{left:383px;width:400px;top:2545px;text-align:center;font-size:12px;line-height:27px;color:var(--white);font-weight:400}
.foot-contact{left:865px;top:2490px;font-size:12px;line-height:26.5px;color:var(--white);font-weight:400}
.foot-contact .web{text-decoration:underline}
</style>
</head>
<body>

<!-- hero -->
<div class="abs hero placeholder" role="img" aria-label="Lys skandinavisk arbeidskrok med hvit stol, skrivebord, lampe og grønn plante i kurv"></div>
<div class="abs logo-box">
  <span class="logo-name">Lumaform</span>
  <span class="logo-tag">FARGE &amp; INTERIØRDESIGN</span>
</div>
<nav class="abs nav">
  <a class="active" href="#">HJEM</a>
  <a href="#">OM LUMAFORM</a>
  <a href="#">TJENESTER OG PRISER</a>
  <a href="#">KONTAKT OSS</a>
</nav>
<svg class="abs flag" width="29" height="17" viewBox="0 0 22 16" aria-label="Norsk">
  <rect width="22" height="16" fill="#ba0c2f"/>
  <rect x="6" width="4" height="16" fill="#fff"/><rect y="6" width="22" height="4" fill="#fff"/>
  <rect x="7" width="2" height="16" fill="#00205b"/><rect y="7" width="22" height="2" fill="#00205b"/>
</svg>
<h1 class="abs script hero-title">Trenger du hjelp til<br>utvikling av interiørmiljøer?</h1>
<p class="abs hero-text">Firma Lumaform AS &nbsp;jobber med utvikling av interiørmiljøer for private, bedrifter<br>og offentlige institusjoner. For å finne de optimale løsninger til et prosjekt,</p>
<a class="btn" style="left:542px;top:417px;width:109px;height:37px">LÆRE MER</a>
<svg class="abs arrow" style="left:183px" width="18" height="30" viewBox="0 0 18 30"><path d="M16 2 3 15l13 13" fill="none" stroke="#333" stroke-width="1.3"/></svg>
<svg class="abs arrow" style="left:993px" width="18" height="30" viewBox="0 0 18 30"><path d="M2 2l13 13L2 28" fill="none" stroke="#333" stroke-width="1.3"/></svg>

<!-- section shapes -->
<svg class="abs" style="left:0;top:0" width="1200" height="2722" viewBox="0 0 1200 2722" aria-hidden="true">
  <polyline points="0,603 592,543 1200,603" fill="none" stroke="var(--grey-line)" stroke-width="4"/>
  <polygon points="0,614 592,553 1200,614 1200,640 0,640" fill="#fff"/>

  <polyline points="0,985 592,920 1200,985" fill="none" stroke="var(--maroon)" stroke-width="3"/>
  <defs>
    <linearGradient id="bizFill" x1="0" y1="0" x2="1" y2="1">
      <stop offset="0" stop-color="#7a2e24"/><stop offset=".5" stop-color="#8a3e33"/><stop offset="1" stop-color="#6e251c"/>
    </linearGradient>
    <linearGradient id="roomFill" x1="0" y1="0" x2="1" y2="0">
      <stop offset="0" stop-color="#c9b1ae"/><stop offset=".45" stop-color="#dcc8c3"/><stop offset=".8" stop-color="#cdb9b0"/><stop offset="1" stop-color="#9aa08f"/>
    </linearGradient>
  </defs>
  <polygon points="0,995 592,928 1200,995 1200,1405 0,1405" fill="url(#bizFill)" role="img" aria-label="Dempet foto av møblert kontorlandskap i rød tone"/>

  <polyline points="0,1852 592,1788 1200,1852" fill="none" stroke="var(--blush-line)" stroke-width="4"/>
  <polygon points="0,1862 592,1797 1200,1862 1200,2345 592,2276 0,2345" fill="url(#roomFill)" role="img" aria-label="Lyst rom med tebord, kopper, bøker og planter"/>

  <polyline points="0,2332 592,2262 1200,2332" fill="none" stroke="var(--night)" stroke-width="3"/>
  <polygon points="0,2342 592,2272 1200,2342 1200,2722 0,2722" fill="var(--night)"/>
</svg>

<!-- welcome -->
<h2 class="abs script welcome-title">Velkommen</h2>
<p class="abs welcome-text">Firma Lumaform AS &nbsp;jobber med utvikling av interiørmiljøer for private, bedrifter og offentlige institusjoner. For å finne de optimale løsninger til et prosjekt, enten det er et rom eller fler, kreves det kjennskap og kunnskap i markedet. Ved å bruke profesjonell kompetanse på området, sparer du både tid og penger.</p>
<a class="btn" style="left:147px;top:860px;width:109px;height:36px">LEARN MORE</a>
<div class="placeholder" role="img" aria-label="Stue med blå sofa, gullbord, lenestol, sort-hvitt teppe og solspeil" style="left:634px;top:623px;width:471px;height:283px;background:radial-gradient(ellipse at 55% 65%,#4b6f86 0%,#8aa2ae 35%,#eef1f2 72%,#fff 100%)"></div>

<!-- business -->
<h2 class="abs script biz-title">Bedrift/ Offentlig</h2>
<p class="abs biz-text">Lumaform hjelper deg med bevisst bruk av materialer i forhold til funksjon,<br>design, forskrifter, pris m.m.</p>
<div class="abs service" style="left:167px;width:164px"><div class="icon" role="img" aria-label="Ikon: klokke"></div>EKSTERIØR/ INTERIØR</div>
<div class="abs service" style="left:344px;width:163px"><div class="icon" role="img" aria-label="Ikon: spisebord"></div>FORM OG UTTRYKK</div>
<div class="abs service" style="left:520px;width:163px"><div class="icon" role="img" aria-label="Ikon: vase"></div>LYS</div>
<div class="abs service" style="left:696px;width:164px"><div class="icon" role="img" aria-label="Ikon: gardiner"></div>EN MØBLERINGSPLAN.</div>
<div class="abs service" style="left:870px;width:164px"><div class="icon" role="img" aria-label="Ikon: taklamper"></div>MARKEDET</div>

<!-- private -->
<div class="placeholder" role="img" aria-label="Hylle i tre med grønn plante og to innrammede bilder" style="left:100px;top:1494px;width:392px;height:214px;background:radial-gradient(ellipse at 50% 60%,#c9a455 0%,#e9dcc0 35%,#f6f3ee 65%,#fff 100%)"></div>
<h2 class="abs script priv-title">Private Interiør</h2>
<p class="abs priv-text">Trenger du veiledning i forhold til stiler, farger, tekstiler eller tresorter? Kanskje du har et gammelt hus som du skal restaurere, eller kanskje du skal bytte kjøkken? Lumaform hjelper deg gjerne med å finne løsninger som er tilpasset deg og dine behov!</p>
<a class="btn" style="left:584px;top:1716px;width:109px;height:36px;font-weight:500">KONTAKT</a>

<!-- features -->
<h2 class="abs script feat-title">Bedrift/ Offentlig</h2>
<div class="abs card card-light" style="left:593px;top:1920px;width:418px;height:137px">
  <h3>EKSTERIØR/ INTERIØR</h3>
  <p>Lumaform hjelper deg med bevisst bruk av materialer<br>i forhold til funksjon,</p>
</div>
<div class="abs card card-light" style="left:155px;top:2075px;width:418px;height:138px">
  <h3>FORM OG UTTRYKK</h3>
  <p>I samarbeid med oppdragsgiver bestrebes det på å<br>få til form og uttykk som skal være tilpasset den</p>
</div>
<div class="abs card card-dark" style="left:593px;top:2075px;width:418px;height:138px">
  <h3>LYS</h3>
  <p>Belysning må fungere med funksjonskrav og bør være<br>beviste handlinger. Planlegging av lys vil ofte være i</p>
</div>

<!-- footer -->
<h4 class="abs foot-head">KONTAKT</h4>
<p class="abs foot-addr">Post/ besøksadresse<br>Lumaform As &nbsp;v/ Ragna Tvedtholm<br>Bryggeveien 14<br>3428 Sandvika</p>
<div class="abs foot-logo"><span class="logo-name">Lumaform</span><span class="logo-tag">FARGE &amp; INTERIØRDESIGN</span></div>
<p class="abs foot-copy">© 2020 Alle rettigheter reservert, Lumaform<br>For å laste ned visittkort, klikk her</p>
<svg class="abs" style="left:551px;top:2626px" width="62" height="28" viewBox="0 0 62 28">
  <circle cx="14" cy="14" r="12.5" fill="none" stroke="#fff" stroke-width="1.5" aria-label="Facebook"/>
  <circle cx="47" cy="14" r="12.5" fill="none" stroke="#fff" stroke-width="1.5" aria-label="Instagram"/>
</svg>
<svg class="abs" style="left:826px;top:2496px" width="18" height="44" viewBox="0 0 18 44" aria-hidden="true">
  <path d="M4 2c-2 1-2 4 0 7s5 6 8 7c2 1 4 0 4-2l-3-2-2 1c-2-1-4-3-5-5l1-2-2-3z" fill="#fff"/>
  <rect x="2" y="32" width="14" height="10" rx="1" fill="#fff"/>
  <path d="M2 33l7 5 7-5" fill="none" stroke="var(--night)" stroke-width="1.2"/>
</svg>
<p class="abs foot-contact">Tlf. +4790000000<br>Mail. post@lumaform-example.no<br><span class="web">Web. www.lumaform-example.no</span></p>

</body>
</html>
```